2023 Cheers to 50 Years Graphic

Hi - I'd like a high-res image that's also print ready that we can use around our office with our 2023 slogan: Cheers to 50 years!

Ideally we'd like a catchy image, the slogan and our logo.

I'll attach the 2022 example. Please use our 50th anniversary logo also attached.

Graphic could be anything celebratory!

Main demographic is males.

Maybe cheers of champagne glasses or beer. But open top option that does not involve alcohol too.

```html
<!DOCTYPE html>
<html lang="en">
<head>
<meta charset="utf-8">
<title>2023 – Cheers to 50 years!</title>
<link rel="stylesheet" href="https://fonts.googleapis.com/css2?family=Lobster&display=swap">
<style>
  :root {
    --ink-blue: #2b3a87;
    --glow-white: #ffffff;
    --spark-core: #fff6dc;
    --spark-gold: #e8b25a;
    --spark-amber: #b47a2c;
    --ember-brown: #4a3417;
    --night-olive: #2a2110;
    --bokeh-yellow: #c9b52e;
  }
  * { margin: 0; padding: 0; box-sizing: border-box; }
  html, body {
    width: 1200px;
    height: 815px;
    overflow: hidden;
    background: var(--night-olive);
  }
  .poster {
    position: relative;
    width: 1200px;
    height: 815px;
    overflow: hidden;
    font-family: "Lobster", cursive;
  }
  .sparkler-photo {
    position: absolute;
    inset: 0;
    background:
      radial-gradient(ellipse 190px 170px at 575px 420px, var(--spark-core) 0%, rgba(255,240,200,0.85) 35%, rgba(232,178,90,0) 100%),
      radial-gradient(ellipse 150px 190px at 150px 620px, rgba(201,181,46,0.75) 0%, rgba(201,181,46,0) 100%),
      radial-gradient(ellipse 620px 460px at 600px 420px, var(--spark-gold) 0%, var(--spark-amber) 45%, var(--ember-brown) 75%, var(--night-olive) 100%);
  }
  .headline {
    position: absolute;
    left: 0;
    width: 100%;
    text-align: center;
    color: var(--ink-blue);
    text-shadow:
      0 0 8px var(--glow-white),
      0 0 14px var(--glow-white),
      0 0 22px rgba(255,255,255,0.8);
    line-height: 1;
    white-space: nowrap;
  }
  .headline-year {
    top: 140px;
    left: -30px;
    font-size: 150px;
  }
  .headline-slogan {
    top: 318px;
    font-size: 118px;
  }
  .brand-mark {
    position: absolute;
    left: 850px;
    top: 656px;
    display: flex;
    align-items: center;
    gap: 12px;
  }
  .brand-dot {
    width: 22px;
    height: 22px;
    border-radius: 50%;
    background: var(--glow-white);
  }
  .brand-name {
    font-family: "Lobster", cursive;
    font-size: 38px;
    color: var(--glow-white);
    line-height: 1;
    white-space: nowrap;
  }
</style>
</head>
<body>
  <main class="poster">
    <div class="sparkler-photo" role="img" aria-label="Close-up photo of a burning sparkler throwing golden sparks against a dark, warm bokeh background"></div>
    <h1 class="headline headline-year">2023</h1>
    <p class="headline headline-slogan">Cheers to 50 years!</p>
    <div class="brand-mark">
      <span class="brand-dot"></span>
      <span class="brand-name">Harborline Supply</span>
    </div>
  </main>
</body>
</html>
```